RESTAURANT MENU

WANTING TO CHANGE MENU DESIGN AND ADD SOME PLATES AND DESSERTS

ILL POST PICTURES OF LOGO AND PLATES. DONT HAVE ANYTHING IN MIND JUST NEED SOMETHING NEW THAT WILL STAND OUT .

Industry/Entity Type

Restaurant

Requirements
Must have
• THE SIZE RIGHT NOW IS 11X17 TRIFOLD MENU.
• IF ITS TOO CROWDED WITH THE NEW PLATES I DONT MIND MAKING IT BIGGER .
• ADD ONS
• ******************************** PASTAS **************************
• CHICKEN FETTUCCINE OR PENNE PASTA - 9.25
• SHRIMP FETTUCCINE OR PENNE PAST 10.25
• ******************* WINGS ***************************************
• BONELESS OR TRADITIONAL
• 5 WINGS - 5.99
• 10 WINGS - 8.99
• 20 WINGS - 14.99
• 50 WINGS - 35.99
• mild , hot , lemon pepper , sweet chili , teriyaki , garlic Parmesan
• *****************FROM THE BAR-B-QUE*************
• BABY BACK RIBS
• half rack - 12.99
• full rack - 18.99
• BRISKET BURGER 8.25
• BARBECUE COMBO - 17.99
• half rack of ribs, brisket , and sausage
• served with potato salad and red beans.
Should not have
• ADRESS CORRECTION ****
• 418 N. MARLOWE AVE.
• ELSA TEXAS
• ************* APPETIZERS***********
• Jalapeno cheese fries ............................. 4.99
• Mozzarella cheese sticks ........................ 5.25
• Classic Nachos ( ground bee) ................. 6.99
• Nachos ( fajita or chicken fajita ).............. 7.99
• Panchos ....................................................8.99
• ( includes lettuce , and avocado )
• Shrimp Nachos ........................................8.99
• Choriqueso...............................................6.99
• Guacamole ..............................................5.99
• ***************SALADS******************
• House Salad ...........................................5.99
• Caesar Salad...........................................5.99
• Chef Salad ...............................................7.99
• Grilled or Crispy chicken Salad ................8.99
• Shrimp Salad ............................................9.99
• ***************BURGERS AND SANDWICHES ****************
• Fajita Steak Burger .............................................................8.95
• (fine cut fajita loaded with fresh sauteed mushrooms , and topped with
• mozzarella cheese, crisp lettuce , onions , tomatoes mayo & mustard)
• Mushroom Swiss Burger .....................................................8.95
• (loaded with fresh saureed mushrooms, and topped with melted Swiss cheese)
• Hawaiian Burger ..................................................................7.99
• (topped with pineapple , american cheese , crisp lettuce , tomatoes and mayo. )
• Barbecue Burger.......................................................................7.99
• (basted with our original Bbq sauce, American cheese , lettuce , fresh tomatoes , mayo and mustard.)
• Patty Melt ................................................................................7.99
• Cheese Burger ........................................................................6.99
• Double Cheese Burger............................................................7.99
• Grilled or Fried Chicken Burger ................................................6.99
• Fish Burger ..............................................................................6.99
• (breaded fish with lettuce, tomatoes & tartar sauce )
• Blt..................................................................................4.99
• (bacon , lettuce & tomato sandwich )
• *******all burgers are served with french fries ***************
• *******ADD THREE SLICES OF BACON TO ANY BURGER ******
• ..................................1.25.
• **************KIDS MENU *****************
• Hamburger combo ..................................3.50
• cheese burger combo ..............................3.99
• Grilled ham and cheese ...........................3.50
• Chicken Tenders .......................................3.99
• Enchilada plate .........................................3.99
• (two enchiladas , rice & beans )
• Ground Beef tacos ...................................3.99
• (2 crispy or soft ground beef tacos , lettuce and cheese )
• ***************SPECIALTIES ***********************
• Chile Relleno ......................................................9.99
• (ground beef or cheese )
• Shrimp and cheese Chile Relleno ......................10.99
• Hamburger steak .................................................8.99
• 8 oz Grilled Chicken Breast .................................8.99
• Chicken Fried Chicken ........................................8.99
• Chicken Fried Steak .............................................8.99
• T Bone .................................................................12.99
• Pork Chops ..........................................................8.99
• Arrachera Steak ...................................................9.99
• ****************COMBINATION PLATES***********************
• Kandry's Special ..................................................8.99
• (fajita with two enchiladas on the side , rice and beans )
• Tampiquena .........................................................9.99
• (fajita steak with two enchiladas on the side , rice and beans
• Rio Bravo Plate .....................................................11.99
• (1 beef or cheese chile relleno with fajita steak on the side , rice and beans )
• Fajita & Shrimp plate .............................................11.99
• T Bone & Shrimp ......................................................13.99
• ************SOUTH OF THE BORDER ****************
• Cheese Enchiladaas ..................................................7.99
• Beef or Chicken Enchiladas ......................................8.99
• Mexican Plate .............................................................9.50
• (three enchiladas , one ground beef taco, and one chicken chalupa )
• Bean and Cheese Chalupa...........................................7.99
• Beef or Chicken Chalupas............................................8.99
• Chicken Flautas ..........................................................8.99
• Beef Milanesa .............................................................8.99
• Chicken Milanesa..........................................................8.99
• Bisteck Ranchero ..........................................................8.99
• Fajita or Chicken plate ...................................................8.99
• Fajita Toreada ................................................................8.99
• Pechuga Santa Fe.........................................................8.99
• Carne Guisada Plate......................................................8.99
• Fajita or Chicken Quesadillas .......................................9.99
• Shrimp Quesadillas ......................................................10.99
• Fajita or Chicken Tacos .................................................8.99
• Ground Beef tacos ( crispy or soft )...............................7.99
• **all Plates are served with rice and beans ***
• ****************TACOS ************
• Chicken fajita taco .....................................2.99
• Fajita taco ..................................................2.99
• Carne guisada ..........................................2.99
• Ground Beef taco ......................................2.50
• ************SOUPS ******************
• Caldo de Res ..........................small 6.99.................large....7.99
• Caldo de Pescado y Camaron ..small 7.99..............large ....8.99
• Caldo Siete Mares .....................small 8.99.............large ....9.99
• Menudo ....................................small ..6.99.............large ..7.99
• Caldo Tlalpeno ..........................small .. 7.99........large 8.99
• *********SEAFOOD*************
• Fish Tacos .................................................8.99
• (fish filet on corn tortilla , rice on the side )
• Fish Plate (Grilled or Fried ).........................11.99
• Shrimp Plate (any style)................................12.99
• (al mojo de ajo, ala diabla, agua chiles , fried)
• Costa Azul ....................................................14.99
• ( 6 shrimp wrapped in bacon and breaded to perfection , filled with mozzarella cheese , served with fries , rice and salad )
• Seafood Fiesta .............................................14.99
• ( combination of fish , shrimp and crab)
• Shrimp Cocktail .......................................small ..9.99.....large...12.99
• ***********FAMILY PLATTERS **************************
• Botana or Sombrero for 1 .............................................10.99
• Botana or Sombrero for 2 ..............................................20.99
• Botana or Sombrero for 3 ..............................................27.99
• Botana or Sombrero for 4 ..............................................38.99
• Botana or Sombrero for 6................................................49.99
• (beef chicken or mixed )
• Seafood platter for 2 ........................................................25.99
• Seafood platter for 3 ........................................................33.99
• Seafood platter for 4 ........................................................44.99
• Seafood platter for 6.........................................................59.99
• Mar y Tierra for 2 ............................................................26.99
• Mar y Tierra for 3 ............................................................35.99
• Mar y Tierra for 4 .............................................................43.99
• Mar y Tierra for 6...............................................................58.99
• *********BREAKFAST PLATES *************************
• Potato & Egg Plate ...................................4.99
• Bacon & Egg Plate ....................................4.99
• Migas & Egg Plate.....................................4.99
• Huevos Rancheros ...................................4.99
• Huevo ala Mexicana ..................................4.99
• Chorizo & Egg Plate ..................................4.99
• Sausage & Egg Plate ................................4.99
• Ham & Egg Plate........................................4.99
• Machacado & Egg Plate ............................5.99
• Chicharron en Salsa.....................................5.99
• Chicharron & Egg Plate................................5.99
• Chicharron en salsa with 2 eggs ..................6.99
• Chilaquiles .................................................5.99
• Huevos Divorciados ...................................6.99
• Chicken Chilaquiles ..................................6.99
• Fajita Asada & egg ......................................7.99
• Barbacoa Plate ............................................6.99
• ( add two eggs )............................................7.99
• **************GOURMET BREAKFAST*****
• Kandry's Favorite .............................................7.99
• two eggs , one slice of ham , two bacon , two sausage links and two buttermilk pancakes
• Kandry's Special ..........................................................3.99
• Two eggs , sausage , ham or bacon
• Ham and cheese Omelette .......................................6.99
• three egg omelette filled with ham and cheese , hash-brown and toast.
• Ultimate Omelette ....................................................7.99
• Three egg omelette with sausage , bacon , fire roasted bell peppers and onion , mushrooms , diced tomatoes and shredded cheese . served with hash-browns and toast .
• Meat lovers Omelette ......................................................8.99
• Three egg omelette with grilled steak , fire roasted bell peppers and onions.
• sauteed mushrooms and melted mozzarella cheese.
• The steakwich ...............................................7.99
• two scrambled eggs, tender steak , american cheese on texas toast .
• Hamwich .......................................................5.99
• sausagewich .................................................5.99
• Chicken Fried steak and eggs .......................7.99
• Pork chops and Eggs .....................................9.99
• T Bone Steak and eggs ...............................10.99
• **********BREAKFAST TACOS ********************
• Bacon & egg ...................1.99
• Sausage & Egg ................1.99
• Potato & Egg...................1.99
• Chorizo & Egg .................1.99
• Bean &Egg.......................1.99
• Ham and Egg ....................1.99
• Machacado & Egg ............2.59
• Chicharron & Egg .............2.59
• Gorditas .............................2.99
• *****extra taco filling *** .35
• *********DRINKS ***********
• Coffee..............................1.99
• Milk ..................................1.99
• Orange Juice ...................2.50
• (no refill )
• Sweet & unsweet Tea ..........2.15
• Raspberry Tea ...................2.50
• Fountain Drinks ..................2.15
• Strawberry lemonade ...........2.50
• Lemonade .............................2.50
• hot chocolate ...........................1.99
• *****15% WILL BE ADDED ON TABLES OF 6 OR MORE ***

```html
<!DOCTYPE html>
<html lang="en">
<head>
<meta charset="utf-8">
<title>Kandry's Trifold Menu</title>
<link href="https://fonts.googleapis.com/css2?family=Rye&family=Arimo:ital,wght@0,400;0,700;1,400&display=swap" rel="stylesheet">
<style>
  :root{
    --bg:#e9e4dc;
    --green:#0e5b2b;
    --green-dark:#083d1c;
    --green-light:#1c7a3c;
    --brown:#5e2c12;
    --brown-dark:#3a1808;
    --brown-light:#7a3d1a;
    --orange:#f29a1f;
    --yellow:#f6c61a;
    --band:#a8962a;
    --text:#f3eee2;
  }
  *{box-sizing:border-box;margin:0;padding:0}
  html,body{width:1200px;height:1200px;overflow:hidden}
  body{background:var(--bg);font-family:"Arimo",sans-serif;color:var(--text);
    display:flex;flex-direction:column;align-items:center;justify-content:center;gap:14px}
  .sheet{width:1140px;height:584px;display:grid;grid-template-columns:repeat(3,1fr);
    box-shadow:0 6px 18px rgba(0,0,0,.25);position:relative}
  .sheet::before,.sheet::after{content:"";position:absolute;top:0;bottom:0;width:10px;background:var(--band);
    box-shadow:inset 0 0 0 2px var(--green-dark);z-index:1}
  .sheet::before{left:0}.sheet::after{right:0}
  .panel{padding:14px 26px 14px;display:flex;flex-direction:column;gap:4px;position:relative;overflow:hidden;
    border-right:1px solid rgba(0,0,0,.25)}
  .panel--green{background:radial-gradient(ellipse at 50% 30%,var(--green-light),var(--green) 55%,var(--green-dark))}
  .panel--brown{background:radial-gradient(ellipse at 50% 30%,var(--brown-light),var(--brown) 55%,var(--brown-dark))}
  .panel:first-child{padding-left:30px}.panel:last-child{padding-right:30px;border-right:0}
  .heading{font-family:"Rye",serif;color:var(--orange);font-size:13px;line-height:1.2;text-transform:uppercase;font-weight:400;
    display:flex;align-items:center;gap:8px;letter-spacing:.5px;margin-top:2px}
  .heading::before,.heading::after{content:"";height:1px;background:var(--orange);flex:0 0 34px}
  .heading::after{flex:1}
  .list{list-style:none;font-size:9px;line-height:1.18}
  .list li{display:flex;align-items:baseline;gap:4px}
  .list li .name{white-space:nowrap}
  .list li .lead{flex:1;border-bottom:1px dotted rgba(243,238,226,.5);transform:translateY(-2px)}
  .list li .price{white-space:nowrap}
  .note{font-style:italic;color:var(--orange);font-size:8px;line-height:1.15;padding-left:6px}
  .section{display:flex;gap:10px;align-items:flex-start}
  .section-body{flex:1;display:flex;flex-direction:column;gap:4px}
  .photo{border-radius:4px;border:3px solid #f4f1ea;flex:0 0 auto;box-shadow:0 2px 6px rgba(0,0,0,.4)}
  .photo--round{border-radius:50%;border-color:var(--orange)}
  .gratuity{background:var(--green);border:1px solid var(--green-light);color:var(--yellow);
    font-family:"Rye",serif;font-size:11px;padding:3px 12px;transform:rotate(-5deg);align-self:center;margin-top:auto;text-align:center;line-height:1.2}
  .call{font-size:14px;color:var(--text);line-height:1.3}
  .call strong{font-family:"Rye",serif;color:var(--orange);font-weight:400;font-size:18px}
  .cover{align-items:center;text-align:center;gap:6px}
  .brand{font-family:"Arimo",sans-serif;font-weight:700;color:var(--yellow);font-size:46px;margin-top:28px;
    display:flex;align-items:center;gap:10px}
  .brand-dot{width:14px;height:14px;border-radius:50%;background:var(--yellow)}
  .tagline{font-family:"Rye",serif;font-size:10.5px;color:var(--text);text-transform:uppercase;line-height:1.35}
  .specialties{background:var(--orange);color:var(--brown-dark);font-style:italic;font-weight:700;font-size:10px;padding:1px 10px;border-radius:2px}
  .menu-tag{position:absolute;right:26px;top:228px;background:var(--yellow);color:var(--brown);font-family:"Rye",serif;
    font-size:16px;padding:3px 10px;border-radius:4px;transform:rotate(-10deg)}
  .hero{width:100%;height:150px;margin-top:10px}
  .contact{font-size:15px;text-align:left;align-self:stretch;display:flex;flex-direction:column;gap:5px;margin-top:auto;margin-bottom:10px}
  .contact strong{font-family:"Rye",serif;color:var(--orange);font-weight:400;font-size:19px}
  .social{display:flex;align-items:center;gap:6px;font-size:11px}
  .social-box{width:14px;height:14px;background:#3b5b9a;border-radius:2px}
  .footnote{font-size:9px;font-weight:700;color:var(--text);margin-top:2px}
  .duo{display:flex;gap:10px;justify-content:center;margin-top:auto;padding-bottom:4px}
</style>
</head>
<body>

<section class="sheet sheet--outside">
  <div class="panel panel--green">
    <h2 class="heading">Breakfast Plates</h2>
    <ul class="list">
      <li><span class="name">Potato &amp; Egg Plate</span><span class="lead"></span><span class="price">4.99</span></li>
      <li><span class="name">Bacon &amp; Egg Plate</span><span class="lead"></span><span class="price">4.99</span></li>
      <li><span class="name">Migas &amp; Egg Plate</span><span class="lead"></span><span class="price">4.99</span></li>
      <li><span class="name">Huevos Rancheros</span><span class="lead"></span><span class="price">4.99</span></li>
      <li><span class="name">Huevo a la Mexicana</span><span class="lead"></span><span class="price">4.99</span></li>
      <li><span class="name">Chorizo &amp; Egg Plate</span><span class="lead"></span><span class="price">4.99</span></li>
      <li><span class="name">Sausage &amp; Egg Plate</span><span class="lead"></span><span class="price">4.99</span></li>
      <li><span class="name">Ham &amp; Egg Plate</span><span class="lead"></span><span class="price">4.99</span></li>
      <li><span class="name">Machacado &amp; Egg Plate</span><span class="lead"></span><span class="price">5.99</span></li>
      <li><span class="name">Chicharron en Salsa</span><span class="lead"></span><span class="price">5.99</span></li>
      <li><span class="name">Chicharron &amp; Egg Plate</span><span class="lead"></span><span class="price">5.99</span></li>
      <li><span class="name">Chicharron en Salsa with 2 Eggs</span><span class="lead"></span><span class="price">6.99</span></li>
      <li><span class="name">Chilaquiles</span><span class="lead"></span><span class="price">5.99</span></li>
      <li><span class="name">Huevos Divorciados</span><span class="lead"></span><span class="price">6.99</span></li>
      <li><span class="name">Chicken Chilaquiles</span><span class="lead"></span><span class="price">6.99</span></li>
      <li><span class="name">Fajita Asada &amp; Egg</span><span class="lead"></span><span class="price">7.99</span></li>
      <li><span class="name">Barbacoa Plate</span><span class="lead"></span><span class="price">6.99</span></li>
    </ul>
    <p class="note">Add two eggs 7.99</p>
    <ul class="list">
      <li><span class="name">Chicken Fried Steak and Eggs</span><span class="lead"></span><span class="price">7.99</span></li>
      <li><span class="name">Pork Chops and Eggs</span><span class="lead"></span><span class="price">9.99</span></li>
      <li><span class="name">T Bone Steak and Eggs</span><span class="lead"></span><span class="price">10.99</span></li>
    </ul>
    <svg class="photo" style="margin-top:auto;margin-bottom:10px;align-self:center" width="230" height="120" role="img" aria-label="Photo of a fajita plate with tortillas and salad">
      <defs><linearGradient id="g-fajita" x1="0" y1="0" x2="1" y2="1"><stop offset="0" stop-color="#c9a15a"/><stop offset=".6" stop-color="#6a3d1c"/><stop offset="1" stop-color="#e8e2d6"/></linearGradient></defs>
      <rect width="230" height="120" fill="url(#g-fajita)"/>
    </svg>
  </div>

  <div class="panel panel--brown">
    <div class="section">
      <div class="section-body">
        <h2 class="heading">Breakfast Tacos</h2>
        <ul class="list">
          <li><span class="name">Bacon &amp; Egg</span><span class="lead"></span><span class="price">1.99</span></li>
          <li><span class="name">Sausage &amp; Egg</span><span class="lead"></span><span class="price">1.99</span></li>
          <li><span class="name">Potato &amp; Egg</span><span class="lead"></span><span class="price">1.99</span></li>
          <li><span class="name">Chorizo &amp; Egg</span><span class="lead"></span><span class="price">1.99</span></li>
          <li><span class="name">Bean &amp; Egg</span><span class="lead"></span><span class="price">1.99</span></li>
          <li><span class="name">Ham &amp; Egg</span><span class="lead"></span><span class="price">1.99</span></li>
          <li><span class="name">Machacado &amp; Egg</span><span class="lead"></span><span class="price">2.59</span></li>
          <li><span class="name">Chicharron &amp; Egg</span><span class="lead"></span><span class="price">2.59</span></li>
          <li><span class="name">Gorditas</span><span class="lead"></span><span class="price">2.99</span></li>
          <li><span class="name">Extra Taco Filling</span><span class="lead"></span><span class="price">.35</span></li>
        </ul>
      </div>
      <svg class="photo" width="90" height="66" style="margin-top:4px" role="img" aria-label="Photo of breakfast tacos"><rect width="90" height="66" fill="#c59a56"/></svg>
    </div>
    <div class="section">
      <div class="section-body">
        <h2 class="heading">Drink</h2>
        <ul class="list">
          <li><span class="name">Coffee</span><span class="lead"></span><span class="price">1.99</span></li>
          <li><span class="name">Milk</span><span class="lead"></span><span class="price">1.99</span></li>
          <li><span class="name">Orange Juice (No Refill)</span><span class="lead"></span><span class="price">2.50</span></li>
          <li><span class="name">Sweet &amp; Unsweet Tea</span><span class="lead"></span><span class="price">2.15</span></li>
          <li><span class="name">Raspberry Tea</span><span class="lead"></span><span class="price">2.50</span></li>
          <li><span class="name">Fountain Drinks</span><span class="lead"></span><span class="price">2.15</span></li>
          <li><span class="name">Strawberry Lemonade</span><span class="lead"></span><span class="price">2.50</span></li>
          <li><span class="name">Lemonade</span><span class="lead"></span><span class="price">2.50</span></li>
          <li><span class="name">Hot Chocolate</span><span class="lead"></span><span class="price">1.99</span></li>
        </ul>
      </div>
      <svg class="photo" width="90" height="60" style="margin-top:4px" role="img" aria-label="Photo of orange juice glasses"><rect width="90" height="60" fill="#e8922a"/></svg>
    </div>
    <h2 class="heading">Pastas</h2>
    <ul class="list">
      <li><span class="name">Chicken Fettuccine or Penne Pasta</span><span class="lead"></span><span class="price">9.25</span></li>
      <li><span class="name">Shrimp Fettuccine or Penne Pasta</span><span class="lead"></span><span class="price">10.25</span></li>
    </ul>
    <div class="section">
      <div class="section-body">
        <h2 class="heading">Wings</h2>
        <ul class="list">
          <li><span class="name">Boneless or Traditional</span></li>
          <li><span class="name">5 Wings</span><span class="lead"></span><span class="price">5.99</span></li>
          <li><span class="name">10 Wings</span><span class="lead"></span><span class="price">8.99</span></li>
          <li><span class="name">20 Wings</span><span class="lead"></span><span class="price">14.99</span></li>
          <li><span class="name">50 Wings</span><span class="lead"></span><span class="price">35.99</span></li>
        </ul>
        <p class="note">Mild, Hot, Lemon Pepper, Sweet Chili, Teriyaki, Garlic Parmesan</p>
      </div>
      <svg class="photo" width="90" height="60" style="margin-top:4px" role="img" aria-label="Photo of chicken wings"><rect width="90" height="60" fill="#7a3a16"/></svg>
    </div>
    <h2 class="heading">From the Bar-B-Que</h2>
    <ul class="list">
      <li><span class="name">Baby Back Ribs &mdash; Half Rack</span><span class="lead"></span><span class="price">12.99</span></li>
      <li><span class="name">Full Rack</span><span class="lead"></span><span class="price">18.99</span></li>
      <li><span class="name">Brisket Burger</span><span class="lead"></span><span class="price">8.25</span></li>
      <li><span class="name">Barbecue Combo</span><span class="lead"></span><span class="price">17.99</span></li>
    </ul>
    <p class="note">Half rack of ribs, brisket and sausage. Served with potato salad and red beans.</p>
    <div class="gratuity">Add a 15% Gratuity<br>on 6 persons or more...</div>
    <p class="call">Call us: <strong>956-555-0148</strong></p>
  </div>

  <div class="panel panel--green cover">
    <div class="brand"><span class="brand-dot"></span>Kandry's</div>
    <p class="tagline">Breakfast, Appetizers,<br>Burgers and Sandwiches</p>
    <span class="specialties">Specialties</span>
    <p class="tagline">South of Border, Combination<br>Plates, Seafood, Soups, Family<br>Platters.... Drinks</p>
    <span class="menu-tag">Menu</span>
    <svg class="hero" viewBox="0 0 320 150" preserveAspectRatio="none" role="img" aria-label="Photo of a cheeseburger with fries">
      <defs><radialGradient id="g-burger" cx=".55" cy=".5" r=".7"><stop offset="0" stop-color="#d39a3a"/><stop offset=".5" stop-color="#7a3f15"/><stop offset="1" stop-color="#2a1206"/></radialGradient></defs>
      <rect width="320" height="150" fill="url(#g-burger)"/>
    </svg>
    <div class="contact">
      <span>Call us: <strong>956-555-0148</strong></span>
      <span>418 N. Marlowe Ave. Elsa Texas</span>
      <span class="social"><span class="social-box"></span>kandrysrestaurant</span>
    </div>
  </div>
</section>

<section class="sheet sheet--inside">
  <div class="panel panel--brown">
    <div class="section">
      <div class="section-body">
        <h2 class="heading">Appetizers</h2>
        <ul class="list">
          <li><span class="name">Jalapeno Cheese Fries</span><span class="lead"></span><span class="price">4.99</span></li>
          <li><span class="name">Mozzarella Cheese Sticks</span><span class="lead"></span><span class="price">5.25</span></li>
          <li><span class="name">Classic Nachos</span><span class="lead"></span><span class="price">6.99</span></li>
          <li><span class="name">Fajita Nachos</span><span class="lead"></span><span class="price">7.99</span></li>
          <li><span class="name">Panchos</span><span class="lead"></span><span class="price">8.99</span></li>
          <li><span class="name">Shrimp Nachos</span><span class="lead"></span><span class="price">8.99</span></li>
          <li><span class="name">Choriqueso</span><span class="lead"></span><span class="price">6.99</span></li>
          <li><span class="name">Guacamole</span><span class="lead"></span><span class="price">5.99</span></li>
        </ul>
      </div>
      <svg class="photo" width="100" height="70" style="margin-top:6px" role="img" aria-label="Photo of nachos with cheese"><rect width="100" height="70" fill="#d8c07a"/></svg>
    </div>
    <h2 class="heading">Salad</h2>
    <ul class="list">
      <li><span class="name">House Salad</span><span class="lead"></span><span class="price">5.99</span></li>
      <li><span class="name">Caesar Salad</span><span class="lead"></span><span class="price">5.99</span></li>
      <li><span class="name">Chef Salad</span><span class="lead"></span><span class="price">7.99</span></li>
      <li><span class="name">Grilled or Crispy Chicken Salad</span><span class="lead"></span><span class="price">8.99</span></li>
      <li><span class="name">Shrimp Salad</span><span class="lead"></span><span class="price">9.99</span></li>
    </ul>
    <h2 class="heading">Burger and Sandwiches</h2>
    <ul class="list">
      <li><span class="name">Fajita Steak Burger</span><span class="lead"></span><span class="price">8.95</span></li>
    </ul>
    <p class="note">Fine cut fajita, sauteed mushrooms, mozzarella, lettuce, onions, tomato, mayo, mustard</p>
    <ul class="list">
      <li><span class="name">Mushroom Swiss Burger</span><span class="lead"></span><span class="price">8.95</span></li>
      <li><span class="name">Patty Melt</span><span class="lead"></span><span class="price">7.99</span></li>
      <li><span class="name">Cheese Burger</span><span class="lead"></span><span class="price">6.99</span></li>
      <li><span class="name">Double Cheese Burger</span><span class="lead"></span><span class="price">7.99</span></li>
      <li><span class="name">Grilled or Fried Chicken Burger</span><span class="lead"></span><span class="price">6.99</span></li>
      <li><span class="name">Fish Burger</span><span class="lead"></span><span class="price">6.99</span></li>
      <li><span class="name">BLT</span><span class="lead"></span><span class="price">4.99</span></li>
      <li><span class="name">Add three slices of bacon to any burger</span><span class="lead"></span><span class="price">1.25</span></li>
    </ul>
    <p class="footnote">All Burgers are served with French Fries</p>
    <div class="duo">
      <svg class="photo photo--round" width="110" height="110" role="img" aria-label="Photo of a cheeseburger"><rect width="110" height="110" fill="#9a5a22"/></svg>
      <svg class="photo photo--round" width="110" height="110" role="img" aria-label="Photo of a sandwich with lettuce"><rect width="110" height="110" fill="#c9a464"/></svg>
    </div>
  </div>

  <div class="panel panel--brown">
    <h2 class="heading">Kids Menu</h2>
    <ul class="list">
      <li><span class="name">Hamburger Combo</span><span class="lead"></span><span class="price">3.50</span></li>
      <li><span class="name">Cheese Burger Combo</span><span class="lead"></span><span class="price">3.99</span></li>
      <li><span class="name">Grilled Ham and Cheese</span><span class="lead"></span><span class="price">3.50</span></li>
      <li><span class="name">Chicken Tenders</span><span class="lead"></span><span class="price">3.99</span></li>
      <li><span class="name">Enchilada Plate</span><span class="lead"></span><span class="price">3.99</span></li>
      <li><span class="name">Ground Beef Tacos</span><span class="lead"></span><span class="price">3.99</span></li>
    </ul>
    <h2 class="heading">Specialties</h2>
    <ul class="list">
      <li><span class="name">Hamburger Steak</span><span class="lead"></span><span class="price">8.99</span></li>
      <li><span class="name">8 oz Grilled Chicken Breast</span><span class="lead"></span><span class="price">8.99</span></li>
      <li><span class="name">Chicken Fried Steak</span><span class="lead"></span><span class="price">8.99</span></li>
      <li><span class="name">T Bone</span><span class="lead"></span><span class="price">12.99</span></li>
      <li><span class="name">Pork Chops</span><span class="lead"></span><span class="price">8.99</span></li>
      <li><span class="name">Arrachera Steak</span><span class="lead"></span><span class="price">9.99</span></li>
    </ul>
    <div class="section">
      <div class="section-body">
        <h2 class="heading">South of Border</h2>
        <ul class="list">
          <li><span class="name">Cheese Enchiladas</span><span class="lead"></span><span class="price">7.99</span></li>
          <li><span class="name">Beef or Chicken Enchiladas</span><span class="lead"></span><span class="price">8.99</span></li>
          <li><span class="name">Mexican Plate</span><span class="lead"></span><span class="price">9.50</span></li>
          <li><span class="name">Chicken Flautas</span><span class="lead"></span><span class="price">8.99</span></li>
          <li><span class="name">Beef Milanesa</span><span class="lead"></span><span class="price">8.99</span></li>
          <li><span class="name">Carne Guisada Plate</span><span class="lead"></span><span class="price">8.99</span></li>
          <li><span class="name">Shrimp Quesadillas</span><span class="lead"></span><span class="price">10.99</span></li>
        </ul>
      </div>
      <svg class="photo" width="100" height="72" style="margin-top:6px" role="img" aria-label="Photo of a Mexican plate"><rect width="100" height="72" fill="#d9a86a"/></svg>
    </div>
    <h2 class="heading">Burger and Sandwiches</h2>
    <ul class="list">
      <li><span class="name">Hawaiian Burger</span><span class="lead"></span><span class="price">7.99</span></li>
    </ul>
    <p class="note">Pineapple, American cheese, crisp lettuce, tomatoes and mayo</p>
    <ul class="list">
      <li><span class="name">Barbecue Burger</span><span class="lead"></span><span class="price">7.99</span></li>
    </ul>
    <p class="note">Our original BBQ sauce, American cheese, lettuce, tomato, mayo, mustard</p>
    <ul class="list">
      <li><span class="name">Patty Melt</span><span class="lead"></span><span class="price">7.99</span></li>
      <li><span class="name">Double Cheese Burger</span><span class="lead"></span><span class="price">7.99</span></li>
      <li><span class="name">Fish Burger</span><span class="lead"></span><span class="price">6.99</span></li>
    </ul>
  </div>

  <div class="panel panel--green">
    <div class="section">
      <div class="section-body">
        <h2 class="heading">Tacos</h2>
        <ul class="list">
          <li><span class="name">Chicken Fajita Taco</span><span class="lead"></span><span class="price">2.99</span></li>
          <li><span class="name">Fajita Taco</span><span class="lead"></span><span class="price">2.99</span></li>
          <li><span class="name">Carne Guisada</span><span class="lead"></span><span class="price">2.99</span></li>
          <li><span class="name">Ground Beef Taco</span><span class="lead"></span><span class="price">2.50</span></li>
        </ul>
      </div>
      <svg class="photo photo--round" width="88" height="88" role="img" aria-label="Photo of shrimp with avocado"><rect width="88" height="88" fill="#d7b89a"/></svg>
    </div>
    <h2 class="heading">Soups</h2>
    <ul class="list">
      <li><span class="name">Caldo de Res</span><span class="lead"></span><span class="price">6.99 / 7.99</span></li>
      <li><span class="name">Caldo de Pescado y Camaron</span><span class="lead"></span><span class="price">7.99 / 8.99</span></li>
      <li><span class="name">Caldo Siete Mares</span><span class="lead"></span><span class="price">8.99 / 9.99</span></li>
      <li><span class="name">Menudo</span><span class="lead"></span><span class="price">6.99 / 7.99</span></li>
      <li><span class="name">Caldo Tlalpeno</span><span class="lead"></span><span class="price">7.99 / 8.99</span></li>
    </ul>
    <h2 class="heading">Sea Food</h2>
    <ul class="list">
      <li><span class="name">Fish Tacos</span><span class="lead"></span><span class="price">8.99</span></li>
      <li><span class="name">Fish Plate (Grilled or Fried)</span><span class="lead"></span><span class="price">11.99</span></li>
      <li><span class="name">Shrimp Plate (Any Style)</span><span class="lead"></span><span class="price">12.99</span></li>
      <li><span class="name">Costa Azul</span><span class="lead"></span><span class="price">14.99</span></li>
      <li><span class="name">Seafood Fiesta</span><span class="lead"></span><span class="price">14.99</span></li>
      <li><span class="name">Shrimp Cocktail</span><span class="lead"></span><span class="price">9.99 / 12.99</span></li>
    </ul>
    <h2 class="heading">Family Platters</h2>
    <ul class="list">
      <li><span class="name">Botana or Sombrero for 1</span><span class="lead"></span><span class="price">10.99</span></li>
      <li><span class="name">Botana or Sombrero for 2</span><span class="lead"></span><span class="price">20.99</span></li>
      <li><span class="name">Botana or Sombrero for 4</span><span class="lead"></span><span class="price">38.99</span></li>
      <li><span class="name">Seafood Platter for 2</span><span class="lead"></span><span class="price">25.99</span></li>
      <li><span class="name">Seafood Platter for 4</span><span class="lead"></span><span class="price">44.99</span></li>
      <li><span class="name">Mar y Tierra for 2</span><span class="lead"></span><span class="price">26.99</span></li>
      <li><span class="name">Mar y Tierra for 4</span><span class="lead"></span><span class="price">43.99</span></li>
    </ul>
    <p class="note">Beef, chicken or mixed</p>
  </div>
</section>

</body>
</html>
```